stationary & business cards for medical clinic
Northfield Institute of Rest Care
stationary & business cards for medical clinic - Medical
Creative Brief
Professional
Delia Marsh
Owner
284 Cobblestone Lane Brookhollow, MS 39402
dmarsh@nirestcare.com
www.nirestcare.com
No color or image on envelope flaps please! No full-bleeds on envelopes or letterhead! Full-bleeds are okay on business cards ONLY.

```html
<!DOCTYPE html>
<html lang="en">
<head>
<meta charset="UTF-8">
<title>Northfield Institute of Rest Care – Business Card</title>
<link href="https://fonts.googleapis.com/css2?family=Open+Sans:wght@400;600;700&display=swap" rel="stylesheet">
<style>
  :root{
    --page:#e9e9e9;
    --card-white:#ffffff;
    --brand-blue:#2f4fa2;
    --brand-blue-deep:#253f8a;
    --accent-red:#e0312b;
    --text-light:#ffffff;
    --logo-blue:#2f6fc0;
  }
  *{margin:0;padding:0;box-sizing:border-box}
  html,body{width:1200px;height:914px;overflow:hidden;background:var(--page);font-family:"Open Sans",Arial,sans-serif}
  .business-card{
    position:absolute;left:100px;top:171px;width:1000px;height:572px;
    background:var(--card-white);overflow:hidden;
    box-shadow:0 6px 18px rgba(0,0,0,.18);
  }
  .card-waves{position:absolute;left:0;top:0;width:1000px;height:572px}
  .brand-mark{
    position:absolute;left:0;right:0;top:150px;
    display:flex;align-items:center;justify-content:center;gap:14px;
  }
  .brand-dot{width:26px;height:26px;border-radius:50%;background:var(--logo-blue)}
  .brand-name{font-size:26px;font-weight:700;color:var(--logo-blue);letter-spacing:.5px}
  .holder{position:absolute;left:300px;top:360px;text-align:right;width:240px;color:var(--text-light)}
  .holder-name{font-size:19px;font-weight:700}
  .holder-title{font-size:14px;margin-top:2px}
  .holder-address{font-size:14px;line-height:1.55;margin-top:28px}
  .contact-list{position:absolute;left:575px;top:362px;list-style:none;color:var(--text-light);font-size:14px}
  .contact-list li{display:flex;align-items:center;gap:10px;height:23px}
  .contact-icon{width:16px;height:16px;flex:none}
</style>
</head>
<body>
<div class="business-card">
  <svg class="card-waves" viewBox="0 0 1000 572" aria-hidden="true">
    <path d="M0 270 C180 250 330 330 500 330 C680 330 820 250 1000 240 L1000 572 L0 572 Z" fill="var(--accent-red)"/>
    <path d="M0 282 C180 262 330 342 500 342 C680 342 820 262 1000 252 L1000 572 L0 572 Z" fill="var(--card-white)"/>
    <path d="M0 300 C180 280 330 356 500 356 C680 356 820 278 1000 268 L1000 572 L0 572 Z" fill="var(--brand-blue)"/>
  </svg>

  <div class="brand-mark">
    <span class="brand-dot"></span>
    <span class="brand-name">Northfield Institute of Rest Care</span>
  </div>

  <div class="holder">
    <div class="holder-name">Delia Marsh</div>
    <div class="holder-title">Owner</div>
    <div class="holder-address">284 Cobblestone Lane Brookhollow<br>MS 39402</div>
  </div>

  <ul class="contact-list">
    <li><svg class="contact-icon" viewBox="0 0 16 16"><circle cx="8" cy="8" r="8" fill="#fff"/><path d="M5 4l2 2-1 1c.5 1.2 1.8 2.5 3 3l1-1 2 2-1.3 1.3C7.7 12 4 8.3 3.7 5.3z" fill="var(--brand-blue)"/></svg>866-555-0142</li>
    <li><svg class="contact-icon" viewBox="0 0 16 16"><circle cx="8" cy="8" r="8" fill="#fff"/><path d="M5 4l2 2-1 1c.5 1.2 1.8 2.5 3 3l1-1 2 2-1.3 1.3C7.7 12 4 8.3 3.7 5.3z" fill="var(--brand-blue)"/></svg>601-555-0187</li>
    <li><svg class="contact-icon" viewBox="0 0 16 16"><circle cx="8" cy="8" r="8" fill="#fff"/><path d="M5 4l2 2-1 1c.5 1.2 1.8 2.5 3 3l1-1 2 2-1.3 1.3C7.7 12 4 8.3 3.7 5.3z" fill="var(--brand-blue)"/></svg>601-555-0120</li>
    <li><svg class="contact-icon" viewBox="0 0 16 16"><circle cx="8" cy="8" r="8" fill="#fff"/><path d="M5 4l2 2-1 1c.5 1.2 1.8 2.5 3 3l1-1 2 2-1.3 1.3C7.7 12 4 8.3 3.7 5.3z" fill="var(--brand-blue)"/></svg>601-555-0163</li>
    <li><svg class="contact-icon" viewBox="0 0 16 16"><circle cx="8" cy="8" r="8" fill="#fff"/><rect x="3.5" y="5" width="9" height="6" fill="var(--brand-blue)"/><path d="M3.5 5l4.5 3.5L12.5 5" stroke="#fff" stroke-width="1" fill="none"/></svg>dmarsh@nirestcare.com</li>
    <li><svg class="contact-icon" viewBox="0 0 16 16"><circle cx="8" cy="8" r="8" fill="#fff"/><circle cx="8" cy="8" r="4.5" stroke="var(--brand-blue)" stroke-width="1.2" fill="none"/><path d="M3.5 8h9M8 3.5c-2 2.5-2 6.5 0 9M8 3.5c2 2.5 2 6.5 0 9" stroke="var(--brand-blue)" stroke-width="1" fill="none"/></svg>www.nirestcare.com</li>
  </ul>
</div>
</body>
</html>
```